Anzeigengestaltung für Zahnarztpraxis
Zielgruppe
Wir sind eine Zahnarztpraxis in einer ländlichen Gemeinde mit 5000 Einwohnern in der Schweiz und bieten alles, was eine moderne Zahnarztpraxis zu bieten hat: Kieferorthopädie, allgemeine Zahnmedizin, Implantologie (schablonengeführt und digital geplant, Clarodent, Intraoralscanner, 3D-Röntgen
Online-Agenda
Zielgruppe: 4-99
2023: 20 jähriges Jubiläum
Der Text sollte später leicht und von uns selbständig geändert werden können:
z.B.
Frühjahrsputz: 20 Franken Rabatt auf die nächste Prophylaxesitzung
Aktion im April: 20% Rabatt auf Clarodent
Aktion im Mai 20% Rabatt auf Implantatbehandlungen
Sommeraktion Bleaching 495.-
Aufgabenstellung
Maße: 185x63mm, (185x130) beide quer
druckoptimiertes PDF X/-4
Bildauflösung: CMYK- und Graustufenbilder 300dpi
Farbprofil: PSOuncoated v3

```html
<!DOCTYPE html>
<html lang="de">
<head>
<meta charset="utf-8">
<title>Praxis Lindner Zahnärzte – 20 Jahre</title>
<link rel="stylesheet" href="https://fonts.googleapis.com/css2?family=Open+Sans:wght@400;600;700&display=swap">
<style>
  :root {
    --green: #84bc3b;
    --green-faint: rgba(255,255,255,0.16);
    --white: #ffffff;
    --frame: #c8c8c8;
    --page: #ffffff;
  }
  * { box-sizing: border-box; margin: 0; padding: 0; }
  html, body { width: 1200px; height: 408px; overflow: hidden; background: var(--page); }
  body { font-family: "Open Sans", Arial, sans-serif; }

  .ad {
    position: relative;
    width: 1200px;
    height: 408px;
    border: 1px solid var(--frame);
    background: var(--page);
  }

  .hero {
    position: absolute;
    left: 19px; top: 19px;
    width: 812px; height: 371px;
    background: var(--green);
    color: var(--white);
    overflow: hidden;
  }
  .hero-mark {
    position: absolute;
    left: 256px; top: 40px;
  }
  .hero-title {
    position: absolute;
    left: 0; right: 0; top: 72px;
    text-align: center;
    font-weight: 700;
    font-size: 116px;
    line-height: 1;
    letter-spacing: -1px;
  }
  .hero-sub {
    position: absolute;
    left: 0; right: 0; top: 212px;
    text-align: center;
    font-weight: 400;
    font-size: 47px;
    line-height: 1;
  }

  .services {
    position: absolute;
    left: 856px; top: 20px;
    width: 330px;
    color: var(--green);
  }
  .services-title {
    font-weight: 600;
    font-size: 24px;
    line-height: 32px;
    margin-bottom: 10px;
  }
  .service-list { list-style: none; }
  .service {
    position: relative;
    padding-left: 30px;
    font-weight: 600;
    font-size: 20px;
    line-height: 27px;
    margin-bottom: 2px;
  }
  .service::before {
    content: "";
    position: absolute;
    left: 1px; top: 5px;
    width: 19px; height: 19px;
    border-radius: 50%;
    background: var(--green);
  }
  .service-note {
    display: block;
    font-weight: 400;
    font-size: 15px;
    line-height: 19px;
    margin: 2px 0 4px;
  }

  .brand {
    position: absolute;
    left: 882px; top: 271px;
    display: flex;
    align-items: center;
    gap: 15px;
  }
  .brand-dot {
    width: 66px; height: 66px;
    border-radius: 50%;
    background: var(--green);
  }
  .brand-name {
    color: var(--green);
    font-weight: 600;
    font-size: 28px;
    line-height: 31px;
  }

  .contact {
    position: absolute;
    left: 856px; top: 352px;
    color: var(--green);
    font-size: 15px;
    line-height: 20px;
  }
</style>
</head>
<body>
  <div class="ad">
    <section class="hero">
      <svg class="hero-mark" width="300" height="300" viewBox="0 0 300 300" aria-hidden="true">
        <circle cx="150" cy="150" r="140" fill="none" stroke="var(--green-faint)" stroke-width="12"/>
      </svg>
      <h1 class="hero-title">Danke,</h1>
      <p class="hero-sub">für 20 Jahre Vertrauen.</p>
    </section>

    <aside class="services">
      <h2 class="services-title">Unsere Leistungen</h2>
      <ul class="service-list">
        <li class="service">Kieferorthopädie</li>
        <li class="service">allgemeine Zahnmedizin</li>
        <li class="service">Implantologie
          <span class="service-note">(schablonengeführt und digital geplant, Clarodent, Intraoralscanner, 3D-Röntgen</span>
        </li>
        <li class="service">Online-Agenda</li>
      </ul>
    </aside>

    <div class="brand">
      <span class="brand-dot"></span>
      <span class="brand-name">Praxis Lindner<br>Zahnärzte</span>
    </div>

    <address class="contact" style="font-style:normal">
      www.praxislindner.ch<br>
      Bergstrasse 12, CH-9044 Wald, St. Gallen
    </address>
  </div>
</body>
</html>
```